I have a small construction company that is growing. I specialize in commercial concrete and custom

I want a site that shows what we do. We specialize in custom deck design and builds. Ridgeline Builders. Commercial concrete . project management

Target Market(s)

Commercial construction companies and custom home builders

Industry/Entity Type

Construction

Number of Pages Required

1 page

Font styles to use
Serif

Colors

Designer to choose colors to be used in the design.

Requirements
Must have
• Pictures and videos of project that we have completed or are in progress

```html
<!DOCTYPE html>
<html lang="en">
<head>
<meta charset="utf-8">
<title>Custom Deck Design and Builds</title>
<link href="https://fonts.googleapis.com/css2?family=Open+Sans:wght@400;600;700;800&display=swap" rel="stylesheet">
<style>
:root{
  --orange:#f5a00f;
  --orange-overlay:rgba(240,168,30,.86);
  --ink:#111418;
  --body:#4a4d52;
  --white:#ffffff;
  --footer:#1f2329;
  --footer-text:#8b9099;
  --dot:#5a5d62;
}
*{margin:0;padding:0;box-sizing:border-box}
html,body{width:1200px;height:3093px;overflow:hidden;background:var(--white)}
body{position:relative;font-family:"Open Sans",Arial,sans-serif;color:var(--ink)}
.abs{position:absolute}
.photo{position:absolute}

/* hero */
.hero{position:absolute;left:0;top:0;width:1200px;height:584px;
  background:linear-gradient(180deg,#5d6b57 0%,#4a5342 30%,#6b5140 62%,#3f4a33 100%)}
.hero-shade{position:absolute;inset:0;background:rgba(20,24,28,.28)}
.brand{position:absolute;display:flex;align-items:center;gap:14px;color:var(--white);
  font-weight:700;font-size:24px;letter-spacing:.3px}
.brand-mark{width:50px;height:50px;border-radius:50%;background:var(--white)}
.hero .brand{left:169px;top:33px}
.menu-btn{position:absolute;left:988px;top:54px;width:46px;height:44px;border:2px solid var(--white);border-width:2px 0 2px 0}
.menu-btn:before,.menu-btn:after{content:"";position:absolute;top:-2px;width:2px;height:44px;background:var(--white)}
.menu-btn:before{left:0;height:10px}
.menu-btn:after{right:0;top:auto;bottom:-2px;height:10px}
.menu-lines{position:absolute;left:13px;top:14px;width:20px;height:13px;
  border-top:2px solid var(--white);border-bottom:2px solid var(--white)}
.menu-lines:after{content:"";position:absolute;left:0;top:3.5px;width:20px;height:2px;background:var(--white)}
.hero-frame{position:absolute;left:278px;top:223px;width:642px;height:148px}
.hero-title{position:absolute;left:0;right:0;top:16px;text-align:center;color:var(--white);
  font-weight:800;font-size:52px;line-height:50px;letter-spacing:.5px}
.btn{position:absolute;display:flex;align-items:center;justify-content:center;border-radius:30px;
  background:var(--orange);color:var(--white);font-weight:700;font-size:11px;letter-spacing:.5px}
.hero .btn{left:522px;top:369px;width:156px;height:48px}
.scroll-tick{position:absolute;left:598px;top:466px;width:3px;height:14px;background:var(--white)}
.hero-tab{position:absolute;left:212px;top:553px;width:774px;height:31px;background:var(--white)}

/* side dot nav */
.dots{position:absolute;left:1133px;display:flex;flex-direction:column;gap:15px}
.dots span{width:7px;height:7px;border-radius:50%;background:var(--dot)}
.dots span.on{background:var(--orange)}
.dots.light span{background:var(--white)}

/* section titles */
.section-title{position:absolute;left:0;width:1200px;text-align:center;font-weight:800;font-size:30px;color:var(--ink)}
.lede{position:absolute;text-align:center;font-size:11px;line-height:20px;color:var(--body)}

/* what we do */
.services-frame{position:absolute;left:483px;top:633px;width:230px;height:202px}
.service{position:absolute;width:230px;text-align:center}
.service svg{display:block;margin:0 auto}
.service h3{margin-top:14px;font-size:12px;font-weight:700;letter-spacing:.3px}
.service p{margin-top:10px;font-size:10px;line-height:17px;color:var(--body)}
.service .more{display:block;margin-top:14px;font-size:8px;font-weight:700;color:var(--orange);letter-spacing:.4px}

/* about */
.about-photo{left:518px;top:1171px;width:682px;height:477px;
  background:linear-gradient(180deg,#6a9fd8 0%,#9cc1e6 42%,#7b746b 58%,#5b5047 82%,#b8a23c 100%)}
.about-panel{position:absolute;left:120px;top:1208px;width:480px;height:406px;background:var(--white)}
.about-title{position:absolute;left:163px;top:1283px;font-weight:800;font-size:30px}
.about-title em{font-style:normal;color:var(--orange)}
.about-text{position:absolute;left:163px;top:1340px;width:340px;font-size:10px;line-height:20.5px;color:var(--body)}
.about .btn{left:163px;top:1511px;width:140px;height:40px}

/* portfolio */
.tile{position:absolute}
.feature-overlay{position:absolute;left:373px;top:1850px;width:452px;height:297px;background:var(--orange-overlay)}
.feature-frame{position:absolute;left:388px;top:1864px;width:422px;height:270px}
.feature-title{position:absolute;left:373px;width:452px;top:1945px;text-align:center;color:var(--white);
  font-weight:800;font-size:21px;line-height:28px;letter-spacing:.5px}
.pill{position:absolute;left:542px;top:2026px;width:114px;height:30px;border-radius:20px;background:var(--white);
  display:flex;align-items:center;justify-content:center;font-size:9px;font-weight:700;color:var(--ink);letter-spacing:.3px}

/* contact */
.contact-item{position:absolute;width:260px;text-align:center}
.contact-item svg{display:block;margin:0 auto}
.contact-item h4{margin-top:12px;font-size:9px;font-weight:700;letter-spacing:3px}
.contact-item p{margin-top:9px;font-size:9px;line-height:15px;font-weight:600;color:var(--orange)}
.contact-item p.link{text-decoration:underline}

/* footer */
.footer{position:absolute;left:0;top:2965px;width:1200px;height:128px;background:var(--footer)}
.footer .brand{left:163px;top:39px}
.copyright{position:absolute;left:464px;top:51px;font-size:9px;line-height:14px;color:var(--footer-text)}
.copyright b{color:var(--white);font-weight:600}
.follow{position:absolute;left:732px;top:58px;font-size:9px;font-weight:600;letter-spacing:.5px;color:var(--white)}
.social{position:absolute;left:830px;top:50px;display:flex;gap:30px}
.social span{width:24px;height:24px;border-radius:50%;background:#555a62}
</style>
</head>
<body>

<!-- Hero -->
<header class="hero">
  <div class="photo" role="img" aria-label="Photo of a finished wooden deck wrapping around a grey family home with garden" style="inset:0;background:inherit"></div>
  <div class="hero-shade"></div>
  <div class="brand"><span class="brand-mark"></span>COMPANY LOGO</div>
  <div class="menu-btn"><span class="menu-lines"></span></div>
  <div class="hero-frame">
    <svg class="abs" width="642" height="148" viewBox="0 0 642 148" fill="none" stroke="#fff" stroke-width="4">
      <path d="M40 2H2V146H40"/><path d="M602 2H640V146H602"/>
    </svg>
    <h1 class="hero-title">CUSTOM DECK DESIGN<br>AND BUILDS</h1>
  </div>
  <a class="btn">KNOW MORE</a>
  <span class="scroll-tick"></span>
  <nav class="dots light" style="top:243px"><span></span><span class="on" style="background:var(--orange)"></span><span></span><span></span></nav>
  <div class="hero-tab"></div>
</header>

<!-- What we do -->
<section class="services">
  <svg class="services-frame" width="230" height="202" viewBox="0 0 230 202" fill="none" stroke="#f5a00f" stroke-width="6">
    <path d="M3 30V3H30"/><path d="M200 3H227V30"/><path d="M3 172V199H30"/><path d="M227 172V199H200"/>
  </svg>
  <h2 class="section-title" style="top:685px">WHAT WE DO</h2>
  <p class="lede" style="left:410px;width:380px;top:733px">Lorem ipsum dolor sit amet, consectetur adipiscing elit, sed do eiusmod tempor incididunt ut labore et dolore magna aliqua. Ut enim ad minim veniam quis nostrud exercitation ullamco laboris nisi</p>
  <nav class="dots" style="top:803px"><span></span><span class="on"></span><span></span><span></span></nav>

  <div class="service" style="left:219px;top:893px">
    <svg width="56" height="56" viewBox="0 0 56 56" fill="none" stroke="#111418" stroke-width="2.4">
      <circle cx="28" cy="31" r="19" fill="#fde3b0"/><path d="M28 20V31L36 35"/><path d="M8 14L16 6M48 14L40 6"/><path d="M16 50L12 54M40 50L44 54"/>
    </svg>
    <h3>SAVE TIME</h3>
    <p>Lorem ipsum dolor sit amet,<br>consectetur adipiscing elit, sed do eiu<br>mod tempor incididunt ut</p>
    <span class="more">READ MORE</span>
  </div>
  <div class="service" style="left:485px;top:893px">
    <svg width="56" height="56" viewBox="0 0 56 56" fill="none" stroke="#111418" stroke-width="2.4">
      <circle cx="28" cy="28" r="10" fill="#fde3b0"/>
      <path d="M24 4H32L33 10L39 13L44 9L50 15L46 21L49 26L55 27V33L49 34L46 40L50 46L44 51L39 47L33 50L32 55H24L23 50L17 47L12 51L6 46L10 40L7 34L1 33V27L7 26L10 21L6 15L12 9L17 13L23 10Z"/>
    </svg>
    <h3>SERVICE</h3>
    <p>Lorem ipsum dolor sit amet,<br>consectetur adipiscing elit, sed do eiu<br>mod tempor incididunt ut</p>
    <span class="more">READ MORE</span>
  </div>
  <div class="service" style="left:747px;top:893px">
    <svg width="56" height="56" viewBox="0 0 56 56" fill="none" stroke="#111418" stroke-width="2.4">
      <circle cx="28" cy="28" r="25"/><circle cx="28" cy="28" r="18" fill="#f5a00f" stroke="none"/><path d="M19 28L26 35L38 22" stroke="#fff" stroke-width="3"/>
    </svg>
    <h3>SATISFACTION</h3>
    <p>Lorem ipsum dolor sit amet,<br>consectetur adipiscing elit, sed do eiu<br>mod tempor incididunt ut</p>
    <span class="more">READ MORE</span>
  </div>
</section>

<!-- About -->
<section class="about">
  <div class="photo about-photo" role="img" aria-label="Photo of a construction site with an excavator, trucks and yellow concrete forms under a blue sky"></div>
  <div class="about-panel"></div>
  <h2 class="about-title">ABOUT <em>US</em></h2>
  <p class="about-text">Lorem ipsum dolor sit amet, consectetur adipiscing elit, sed do eiusmod tempor incididunt ut labore et dolore magna aliqua. Ut enim ad minim veniam, quis nostrud exercitation ullamco laboris nisi ut aliquip ex ea commodo consequat. Duis aute irure dolor in reprehenderit in voluptate velit esse cillum dolore eu fugiat nulla pariatur. Excepteur sint occaecat cupidatat non proident, sunt in culpa qui officia deserunt mollit anim id laborum enim ad minim veniam, quis nostrud exercitation.</p>
  <a class="btn">READ MORE</a>
  <nav class="dots light" style="top:1358px"><span></span><span></span><span></span><span></span><span></span></nav>
</section>

<!-- Portfolio -->
<section class="portfolio">
  <h2 class="section-title" style="top:1748px">PORTFOLIO</h2>
  <p class="lede" style="left:0;width:1200px;top:1798px">Lorem ipsum dolor sit amet, consectetur adipiscing elit, sed do</p>

  <div class="tile" role="img" aria-label="Photo of a two-level cedar deck with stairs beside a beige house" style="left:0;top:1850px;width:373px;height:297px;background:linear-gradient(160deg,#5f8a4a,#b58a5c 55%,#8a5a3a)"></div>
  <div class="tile" role="img" aria-label="Photo of a resort deck project" style="left:373px;top:1850px;width:452px;height:297px;background:linear-gradient(160deg,#8a8a6a,#c09a60)"></div>
  <div class="feature-overlay"></div>
  <svg class="feature-frame" width="422" height="270" viewBox="0 0 422 270" fill="none" stroke="#fff" stroke-width="2">
    <path d="M1 26V1H26"/><path d="M396 1H421V26"/><path d="M1 244V269H26"/><path d="M421 244V269H396"/>
  </svg>
  <h3 class="feature-title">HARBOR AND PINE<br>RESORT</h3>
  <a class="pill">VIEW DETAILS</a>
  <div class="tile" role="img" aria-label="Photo of a patio deck with blue cushioned bench and fire table" style="left:825px;top:1850px;width:375px;height:297px;background:linear-gradient(160deg,#7a6a5a,#3f5d8a 50%,#5d4a3a)"></div>
  <div class="tile" role="img" aria-label="Photo of a red-stained deck with a pergola surrounded by trees" style="left:0;top:2147px;width:600px;height:395px;background:linear-gradient(170deg,#3f6a3a,#9a3f2a 45%,#c08050)"></div>
  <div class="tile" role="img" aria-label="Photo of a modern house with orange wood cladding and a garden patio" style="left:600px;top:2147px;width:600px;height:395px;background:linear-gradient(160deg,#4a78b8,#d07a30 40%,#4f6a3a 75%,#9a9a90)"></div>
  <nav class="dots" style="top:2070px"><span></span><span></span><span></span><span class="on"></span><span></span></nav>
</section>

<!-- Contact -->
<section class="contact">
  <h2 class="section-title" style="top:2645px">CONTACT INFORMATION</h2>
  <p class="lede" style="left:0;width:1200px;top:2691px">Lorem ipsum dolor sit amet, consectetur adipiscing elit, sed do</p>
  <nav class="dots" style="top:2702px"><span></span><span></span><span></span><span></span><span class="on"></span></nav>

  <div class="contact-item" style="left:206px;top:2776px">
    <svg width="34" height="34" viewBox="0 0 34 34" fill="none" stroke="#111418" stroke-width="2.2">
      <path d="M8 3L13 10L10 14C12 19 15 22 20 24L24 21L31 26L27 31C16 30 4 18 3 7Z"/>
      <path d="M20 3A11 11 0 0 1 31 14" stroke="#f5a00f"/><path d="M20 8A6 6 0 0 1 26 14" stroke="#f5a00f"/>
    </svg>
    <h4>PHONE</h4>
    <p class="link">(555) 014-2290</p>
  </div>
  <div class="contact-item" style="left:468px;top:2776px">
    <svg width="34" height="34" viewBox="0 0 34 34" fill="none" stroke="#111418" stroke-width="2.2">
      <path d="M17 32C10 22 6 17 6 12A11 11 0 0 1 28 12C28 17 24 22 17 32Z"/><circle cx="17" cy="12" r="4" fill="#f5a00f" stroke="none"/>
    </svg>
    <h4>LOCATION</h4>
    <p>410 Quarry Road (Unit 12)<br>Suite B Ridgeview UT 84000 USA</p>
  </div>
  <div class="contact-item" style="left:732px;top:2776px">
    <svg width="34" height="34" viewBox="0 0 34 34" fill="none" stroke="#111418" stroke-width="2.2">
      <rect x="3" y="9" width="28" height="20"/><path d="M3 9L17 20L31 9"/><path d="M10 9V4H24V9" stroke="#f5a00f"/>
    </svg>
    <h4>EMAIL</h4>
    <p class="link">info@ridgeline.example</p>
  </div>
</section>

<!-- Footer -->
<footer class="footer">
  <div class="brand"><span class="brand-mark"></span>COMPANY LOGO</div>
  <p class="copyright">© 2018 <b>Ridgeline Builders</b><br>All rights reserved.</p>
  <span class="follow">FOLLOW US:</span>
  <div class="social" aria-label="Social links"><span></span><span></span><span></span><span></span></div>
</footer>

</body>
</html>
```